Fun Location App for users to earn rewards and vouchers everywhere they go

Jorvix is a social app where users can collect rewards when they travel + complete quests at different location to get rewards.

We would like a design of an app that has these features/function
1) Login/Signup Page
2) HomePage - A Map with your current location
- Show the location/stores aroudn
- Have a bag tab to press and get rewards
3) Quests Tab = show all the available tasks
4) Exchange Tab = all the items available for exchange vouchers and can click to know more
5) Wallet Tab = user profile + vouchers in their wallet
6) Partners Tab = Showcase all the partners and can click to know more
7) Claim functions

We have attached a visual example. Do feel free to change what is best fit too. We do need to exact measurements as well to create the app

Target Market(s)

Fun, people who like rewards and interact with friends

Font styles to use
Sans Serif

Colors
f78f20
fbed22
fbee3e

Requirements
Must have
• Yellow, fun interactive feeling.
Nice to have
• Pop up when click on things
Should not have
• nil

```html
<!DOCTYPE html>
<html lang="en">
<head>
<meta charset="utf-8">
<title>Jorvix – Login &amp; Signup</title>
<link rel="stylesheet" href="https://fonts.googleapis.com/css2?family=Quicksand:wght@300;400;500;600;700&display=swap">
<style>
  :root{
    --bg:#2a2a2a;
    --orange:#f78f20;
    --yellow:#fbed22;
    --yellow-soft:#fbee3e;
    --white:#ffffff;
    --ink:#111111;
    --muted:#d6d6d6;
    --field-border:#e3e3e3;
    --placeholder:#a8a8a8;
  }
  *{box-sizing:border-box;margin:0;padding:0}
  html,body{width:1200px;height:1200px;overflow:hidden}
  body{background:var(--bg);font-family:"Quicksand",sans-serif;position:relative}

  .brand{position:absolute;left:66px;top:128px;display:flex;align-items:center;gap:14px}
  .brand__dot{width:30px;height:30px;border-radius:50%;background:var(--yellow)}
  .brand__name{font-size:58px;font-weight:700;color:var(--orange);line-height:1}

  .screen{position:absolute;top:239px;width:375px;height:851px;border-radius:37px;overflow:hidden;
    background:linear-gradient(180deg,var(--orange) 0%,#f9b325 45%,var(--yellow-soft) 100%)}
  .screen--signup{left:222px}
  .screen--login{left:717px}

  .welcome{position:absolute;left:0;right:0;top:82px;text-align:center;color:var(--ink);
    font-size:31px;font-weight:400;line-height:1}
  .title{position:absolute;left:0;right:0;top:103px;text-align:center;color:var(--white);
    font-size:68px;font-weight:700;line-height:1;letter-spacing:1px}
  .lead{position:absolute;left:37px;top:232px;color:var(--white);font-size:20px;font-weight:600;line-height:24px}

  .card{position:absolute;left:21px;width:331px;top:271px;background:var(--white);border-radius:25px;
    box-shadow:0 8px 20px rgba(180,100,0,.18)}
  .screen--signup .card{height:402px}
  .screen--login .card{height:295px}

  .tab{position:absolute;top:20px;font-size:17px;font-weight:700;line-height:20px;color:#dcdcdc;text-transform:uppercase}
  .tab--active{color:var(--ink)}
  .tab--active::after{content:"";position:absolute;left:0;right:0;bottom:-4px;height:2px;background:var(--orange)}
  .tab--left{left:42px}
  .tab--right{right:42px}

  .field{position:absolute;left:22px;width:292px;height:50px;border:1.5px solid var(--field-border);
    border-radius:25px;display:flex;align-items:center}
  .field svg{position:absolute;left:20px;width:22px;height:22px}
  .field__text{position:absolute;left:61px;font-size:12.5px;color:var(--placeholder)}

  .gender{position:absolute;top:270px;display:flex;align-items:center;gap:14px;font-size:14px;
    font-weight:700;line-height:30px;color:var(--muted)}
  .gender__mark{width:30px;height:30px;border-radius:50%;border:1.2px solid var(--muted);display:flex;
    align-items:center;justify-content:center}
  .gender__mark--on{background:#a9a9a9;border-color:#a9a9a9}
  .gender__mark svg{width:16px;height:16px}

  .terms{position:absolute;left:0;right:0;top:335px;text-align:center;font-size:10.5px;line-height:16px;color:#9a9a9a}
  .terms__link{color:var(--orange);font-weight:700;text-decoration:underline;text-underline-offset:2px}

  .forgot{position:absolute;right:31px;top:202px;font-size:13px;line-height:16px;color:#b0b0b0}

  .submit{position:absolute;width:84px;height:84px;left:145px;border-radius:50%;background:var(--white);
    display:flex;align-items:center;justify-content:center}
  .submit__btn{width:50px;height:50px;border-radius:50%;
    background:linear-gradient(180deg,#fbc52a,var(--orange));box-shadow:0 4px 8px rgba(200,110,0,.35);
    display:flex;align-items:center;justify-content:center}
  .submit__btn svg{width:20px;height:20px}
  .screen--signup .submit{top:632px}
  .screen--login .submit{top:524px}

  .amp{position:absolute;left:0;right:0;text-align:center;color:var(--white);font-size:20px;font-weight:700;line-height:24px}
  .create{position:absolute;left:0;right:0;text-align:center;color:var(--orange);font-size:20px;font-weight:700;line-height:24px}
  .screen--signup .amp{top:731px}
  .screen--signup .create{top:762px}
  .screen--login .amp{top:624px}
  .screen--login .create{top:655px}
</style>
</head>
<body>
  <div class="brand">
    <span class="brand__dot"></span>
    <span class="brand__name">jorvix</span>
  </div>

  <svg width="0" height="0" style="position:absolute">
    <defs>
      <symbol id="icon-user" viewBox="0 0 24 24"><g fill="none" stroke="#b5b5b5" stroke-width="1.2"><circle cx="12" cy="8" r="4.5"/><path d="M3.5 22c0-5 3.8-8 8.5-8s8.5 3 8.5 8"/></g></symbol>
      <symbol id="icon-mail" viewBox="0 0 24 24"><g fill="none" stroke="#b5b5b5" stroke-width="1.2"><rect x="2" y="5" width="20" height="14" rx="1"/><path d="M2 5l10 8 10-8M2 19l7.5-7M22 19l-7.5-7"/></g></symbol>
      <symbol id="icon-lock" viewBox="0 0 24 24"><g fill="none" stroke="#b5b5b5" stroke-width="1.2"><rect x="3" y="10" width="14" height="12" rx="1.5"/><path d="M6 10V7a4 4 0 0 1 8 0v3"/><circle cx="18" cy="18" r="4"/><path d="M16.4 18l1.2 1.2 2-2"/></g></symbol>
      <symbol id="icon-arrow" viewBox="0 0 24 24"><path d="M3 12h17M14 6l6 6-6 6" fill="none" stroke="#fff" stroke-width="2" stroke-linecap="round" stroke-linejoin="round"/></symbol>
    </defs>
  </svg>

  <section class="screen screen--signup">
    <p class="welcome">welcome to</p>
    <h1 class="title">jorvix</h1>
    <p class="lead">Signup to Continue</p>
    <div class="card">
      <span class="tab tab--left">Login</span>
      <span class="tab tab--right tab--active">Signup</span>
      <div class="field" style="top:73px"><svg><use href="#icon-user"/></svg><span class="field__text">User Name</span></div>
      <div class="field" style="top:140px"><svg><use href="#icon-mail"/></svg><span class="field__text">Email</span></div>
      <div class="field" style="top:207px"><svg><use href="#icon-lock"/></svg><span class="field__text">Password</span></div>
      <div class="gender" style="left:51px"><span class="gender__mark gender__mark--on"><svg viewBox="0 0 24 24"><g fill="none" stroke="#fff" stroke-width="1.5"><circle cx="12" cy="8" r="4.5"/><path d="M3.5 22c0-5 3.8-8 8.5-8s8.5 3 8.5 8"/></g></svg></span>Male</div>
      <div class="gender" style="left:183px"><span class="gender__mark"><svg><use href="#icon-user"/></svg></span>Female</div>
      <p class="terms">By pressing 'Submit' you agree to<br>our <span class="terms__link">terms &amp; conditions</span></p>
    </div>
    <div class="submit"><div class="submit__btn"><svg><use href="#icon-arrow"/></svg></div></div>
    <p class="amp">&amp;</p>
    <p class="create">Create A New Account</p>
  </section>

  <section class="screen screen--login">
    <p class="welcome">welcome to</p>
    <h1 class="title">jorvix</h1>
    <p class="lead">Signup to Continue</p>
    <div class="card">
      <span class="tab tab--left tab--active">Login</span>
      <span class="tab tab--right">Signup</span>
      <div class="field" style="top:74px"><svg><use href="#icon-mail"/></svg><span class="field__text">Email/User Name</span></div>
      <div class="field" style="top:141px"><svg><use href="#icon-lock"/></svg><span class="field__text">Password</span></div>
      <p class="forgot">Forgot Password?</p>
    </div>
    <div class="submit"><div class="submit__btn"><svg><use href="#icon-arrow"/></svg></div></div>
    <p class="amp">&amp;</p>
    <p class="create">Create A New Account</p>
  </section>
</body>
</html>
```